Agricultural Consulting Website

Provide a modern yet business like website for my new Agriculture Consulting Business in Australia called FieldNorth. Whilst we are based in Australia we are targetting both domestic and international markets (especially in Asia). We are targetting corporate, small business, government and farmer clients. The design should compliment our logo also sourced through pixel harbor. The webiste should be easy for me to keep updated on a regular basis without the need to go back to the designer.

Industry/Entity Type

Business

Requirements
Must have
• clean crisp feel
• be modern yet business like
• be able to be updated by myself easily

```html
<!DOCTYPE html>
<html lang="en">
<head>
<meta charset="utf-8">
<title>FieldNorth – Agricultural Consulting</title>
<link href="https://fonts.googleapis.com/css2?family=Arimo:wght@400;700&display=swap" rel="stylesheet">
<style>
:root{
  --brown:#6b3a0c;
  --green:#5f9a05;
  --green-soft:#9dbf5f;
  --orange-top:#f0954a;
  --orange-bottom:#e56f2c;
  --text:#6a6a6a;
  --rule:#dcdcdc;
  --header-bg:#f5f3f3;
  --white:#ffffff;
}
*{margin:0;padding:0;box-sizing:border-box}
html,body{width:1012px;height:1200px;overflow:hidden;background:var(--white)}
body{position:relative;font-family:"Arimo",Arial,sans-serif;color:var(--text)}
.abs{position:absolute}
.site-header{left:0;top:0;width:1012px;height:57px;background:var(--header-bg)}
.brand{left:120px;top:10px;display:flex;align-items:center;gap:7px}
.brand-mark{width:32px;height:32px;background:var(--green)}
.brand-name{font-size:28px;color:var(--green);font-weight:400;line-height:1}
.main-nav{left:0;top:14px;width:1012px;height:32px}
.main-nav a{position:absolute;top:0;height:32px;line-height:32px;font-size:12px;color:var(--brown);text-decoration:none;transform:translateX(-50%);white-space:nowrap}
.main-nav a.active{background:var(--green-soft);color:var(--white);width:57px;text-align:center}
.hero{left:0;top:57px;width:1012px;height:331px;background:linear-gradient(180deg,#d8cfcf 0%,#e3dada 45%,#7f9a52 65%,#4a7a24 100%)}
.hero-title{left:0;top:98px;width:1012px;text-align:center;font-size:42px;font-weight:400;color:var(--brown)}
.hero-sub{left:0;top:165px;width:1012px;text-align:center;font-size:15px;color:#2a2a2a}
.hero-arrow{top:198px}
.service-photo{width:208px;height:208px;border-radius:50%;border:5px solid var(--white);top:283px}
.service{width:220px;text-align:center}
.service h3{font-size:16px;color:var(--brown);font-weight:700;letter-spacing:.3px}
.service p{margin-top:14px;font-size:10.5px;line-height:16px;color:var(--text)}
.btn{display:inline-block;background:linear-gradient(180deg,var(--orange-top),var(--orange-bottom));color:var(--white);font-size:11px;font-weight:700;text-align:center;width:87px;height:32px;line-height:32px;text-decoration:none}
.service .btn{margin-top:19px}
.rule{left:130px;top:669px;width:752px;height:1px;background:var(--rule)}
.section-title{font-size:22px;color:var(--brown);font-weight:700}
.about-photo{left:130px;top:732px;width:224px;height:197px;background:linear-gradient(180deg,#a9b98f 0%,#6e4a2e 100%)}
.about-lead{left:383px;top:734px;font-size:14.5px;color:var(--green);font-weight:400;letter-spacing:.3px}
.about-copy{left:380px;width:502px;font-size:10.4px;line-height:16px}
.news-item{top:1004px;width:250px;display:flex;gap:11px}
.news-item p{width:192px;font-size:10.4px;line-height:16px}
.site-footer{left:0;top:1123px;width:1012px;height:77px;background:var(--green)}
.footer-nav{left:124px;top:31px;font-size:10px;color:var(--white);white-space:nowrap}
.footer-nav span{margin:0 11px}
.copyright{left:520px;width:254px;top:31px;font-size:9.6px;color:var(--white);text-align:right;white-space:nowrap}
.social{left:792px;top:28px;display:flex;gap:5px}
.social span{width:21px;height:21px;border-radius:50%;background:var(--white)}
</style>
</head>
<body>
<header class="site-header abs">
  <div class="brand abs"><span class="brand-mark"></span><span class="brand-name">FieldNorth</span></div>
  <nav class="main-nav abs">
    <a class="active" style="left:423px">Home</a>
    <a style="left:506px">About</a>
    <a style="left:594px">Activities</a>
    <a style="left:686px">Events</a>
    <a style="left:778px">Members</a>
    <a style="left:872px">Contact</a>
  </nav>
</header>

<section class="hero abs" role="img" aria-label="Wide photo of green crop rows stretching to the horizon under a streaked sky"></section>
<h1 class="hero-title abs">FieldNorth</h1>
<p class="hero-sub abs">Lorem ipsum dolor sit ametcon seradipi scitelit.esent vestibulumoles tielacus lorete.</p>
<svg class="hero-arrow abs" style="left:153px" width="34" height="34" viewBox="0 0 34 34"><circle cx="17" cy="17" r="16" fill="none" stroke="#ffffff" stroke-opacity=".5" stroke-width="2"/><path d="M20 10l-7 7 7 7" fill="none" stroke="#ffffff" stroke-opacity=".6" stroke-width="3"/></svg>
<svg class="hero-arrow abs" style="left:818px" width="34" height="34" viewBox="0 0 34 34"><circle cx="17" cy="17" r="16" fill="none" stroke="#ffffff" stroke-opacity=".5" stroke-width="2"/><path d="M14 10l7 7-7 7" fill="none" stroke="#ffffff" stroke-opacity=".6" stroke-width="3"/></svg>

<div class="service-photo abs" style="left:138px;background:#d9b8a0" role="img" aria-label="Photo of cupped hands holding soil with a young seedling"></div>
<div class="service-photo abs" style="left:406px;background:#3f8a22" role="img" aria-label="Photo of rows of green crops under a blue sky"></div>
<div class="service-photo abs" style="left:668px;background:#7a7060" role="img" aria-label="Photo of a hand holding a clump of dark soil over grass"></div>

<div class="service abs" style="left:132px;top:508px"><h3>SMALL BUSINESS</h3><p>Lorem ipsum dolor sit ametcon<br>seradipi scitelit.esent vestibu-<br>lumoles tielacus lorete.</p><a class="btn">Read More</a></div>
<div class="service abs" style="left:400px;top:508px"><h3>GOVERNMENT</h3><p>Lorem ipsum dolor sit ametcon<br>seradipi scitelit.esent vestibu-<br>lumoles tielacus lorete.</p><a class="btn">Read More</a></div>
<div class="service abs" style="left:662px;top:508px"><h3>FARMER CLIENTS</h3><p>Lorem ipsum dolor sit ametcon<br>seradipi scitelit.esent vestibu-<br>lumoles tielacus lorete.</p><a class="btn">Read More</a></div>

<div class="rule abs"></div>

<h2 class="section-title abs" style="left:131px;top:686px">About us</h2>
<div class="about-photo abs" role="img" aria-label="Photo of a ploughed field with crop rows and a single tree on a hill"></div>
<h3 class="about-lead abs">LOREM IPSUM DOLOR SIT AMET CONS ADIPI SCING ELI ESEN.</h3>
<p class="about-copy abs" style="top:760px">It is a long established fact that a reader will be distracted by the readable content of a page when looking at its layout. The point of using Lorem Ipsum is that it has a more-or-less normal distribution of letters, as opposed to using 'Content here, content here', making it look like readable English. Many desktop publishing packages and web page editors.</p>
<p class="about-copy abs" style="top:855px">It is a long established fact that a reader will be distracted by the readable content of a page when looking at its layout. The point of using Lorem Ipsum is that it has a more-or-less normal distribution of letters, as opposed to using 'Content here, content here...</p>
<a class="btn abs" style="left:794px;top:899px;height:33px;line-height:33px">Read More</a>

<h2 class="section-title abs" style="left:132px;top:957px">News &amp;Events</h2>
<div class="news-item abs" style="left:137px">
  <svg width="25" height="25" viewBox="0 0 25 25"><circle cx="12.5" cy="12.5" r="12.5" fill="#c9c9c9"/><path d="M11 8l4.5 4.5L11 17" fill="none" stroke="#fff" stroke-width="2.2"/></svg>
  <p>It is a long established fact that a reader will be distracted by the readable content of a page when looking at its layout. The point of using Lorem Ipsum is that it has a more-or-less normal...</p>
</div>
<div class="news-item abs" style="left:390px">
  <svg width="25" height="25" viewBox="0 0 25 25"><circle cx="12.5" cy="12.5" r="12.5" fill="#c9c9c9"/><path d="M11 8l4.5 4.5L11 17" fill="none" stroke="#fff" stroke-width="2.2"/></svg>
  <p>It is a long established fact that a reader will be distracted by the readable content of a page when looking at its layout. The point of using Lorem Ipsum is that it has a more-or-less normal...</p>
</div>
<div class="news-item abs" style="left:651px">
  <svg width="25" height="25" viewBox="0 0 25 25"><circle cx="12.5" cy="12.5" r="12.5" fill="#c9c9c9"/><path d="M11 8l4.5 4.5L11 17" fill="none" stroke="#fff" stroke-width="2.2"/></svg>
  <p>It is a long established fact that a reader will be distracted by the readable content of a page when looking at its layout. The point of using Lorem Ipsum is that it has a more-or-less normal...</p>
</div>

<footer class="site-footer abs">
  <div class="footer-nav abs">Home<span>|</span>About<span>|</span>Activities<span>|</span>Events<span>|</span>Members<span>|</span>Contact</div>
  <div class="copyright abs">copyright © 2013 FieldNorth all right reserved.</div>
  <div class="social abs"><span></span><span></span><span></span><span></span></div>
</footer>
</body>
</html>
```